Quorvan Medical business cards

Double sided business cards.

Medical technology consulting company.

Business cards with two names on the front, upper to middle left:

Dr Colin R. Harbury BMed GAICD +61412558907
Dr Owen Palatsky PhD MCommrclLaw +61437619042

Email and website addresses bottom right:

colin@quorvanmedical.com.au
www.quorvanmedical.com.au

Tree logo (as per attached file) on front in a suitable position.

Tag line (as per attached files) on the back.

Need a file format to upload to Paper Haven or Cardlyner.

```html
<!DOCTYPE html>
<html lang="en">
<head>
<meta charset="utf-8">
<title>Quorvan Medical – Business Cards</title>
<link rel="stylesheet" href="https://fonts.googleapis.com/css2?family=Poppins:wght@400;700;800&family=Lato:wght@400&display=swap">
<style>
  :root {
    --backdrop: #403e3f;
    --card: #ffffff;
    --maroon: #5a0f0c;
    --leaf: #4a9340;
    --tagline: #5b9b1d;
  }
  * { margin: 0; padding: 0; box-sizing: border-box; }
  html, body { width: 1200px; height: 1200px; overflow: hidden; }
  body { background: var(--backdrop); position: relative; font-family: "Poppins", sans-serif; }

  .card {
    position: absolute;
    left: 291px;
    width: 651px;
    height: 381px;
    background: var(--card);
    box-shadow: 0 6px 18px rgba(0,0,0,0.35);
  }
  .card--brand { top: 242px; }
  .card--contact { top: 648px; }

  .brand-name {
    position: absolute;
    left: 0; right: 0;
    top: 228px;
    text-align: center;
    font-family: "Poppins", sans-serif;
    font-weight: 400;
    font-size: 40px;
    letter-spacing: 0.5px;
    color: var(--maroon);
  }
  .brand-mark {
    position: absolute;
    left: 50%;
    top: 120px;
    width: 70px; height: 70px;
    margin-left: -35px;
    border-radius: 50%;
    background: var(--leaf);
  }
  .tagline {
    position: absolute;
    left: 0; right: 0;
    top: 293px;
    text-align: center;
    font-family: "Lato", sans-serif;
    font-size: 23.5px;
    color: var(--tagline);
    white-space: nowrap;
  }
  .tagline .divider { font-size: 16px; margin: 0 8px; position: relative; top: -2px; }

  .people {
    position: absolute;
    left: 56px;
    top: 50px;
    color: var(--maroon);
    font-size: 19px;
    line-height: 24.2px;
  }
  .person-name strong { font-weight: 800; }
  .phone { display: flex; align-items: center; gap: 8px; padding-left: 4px; }
  .phone svg { width: 16px; height: 16px; fill: var(--leaf); }

  .web-contact {
    position: absolute;
    left: 45px;
    top: 285px;
    color: var(--maroon);
    font-size: 19px;
    line-height: 24.5px;
  }
  .web-contact .row { display: flex; align-items: center; gap: 6px; }
  .web-contact svg { width: 20px; height: 18px; }
  .web-contact strong { font-weight: 700; }

  .corner-name {
    position: absolute;
    left: 420px;
    top: 238px;
    width: 200px;
    text-align: center;
    font-weight: 400;
    font-size: 22px;
    color: var(--maroon);
  }
</style>
</head>
<body>

<section class="card card--brand">
  <div class="brand-mark"></div>
  <h1 class="brand-name">QUORVAN MEDICAL</h1>
  <p class="tagline">Concept<span class="divider">|</span>Commercialisation<span class="divider">|</span>Beyond</p>
</section>

<section class="card card--contact">
  <div class="people">
    <div class="person-name">Dr Colin R. Harbury <strong>BMed GAICD</strong></div>
    <div class="phone">
      <svg viewBox="0 0 24 24"><path d="M6.6 10.8a15.1 15.1 0 0 0 6.6 6.6l2.2-2.2c.3-.3.7-.4 1-.2 1.1.4 2.3.6 3.6.6.6 0 1 .4 1 1V20c0 .6-.4 1-1 1A17 17 0 0 1 3 4c0-.6.4-1 1-1h3.5c.6 0 1 .4 1 1 0 1.3.2 2.5.6 3.6.1.3 0 .7-.2 1z"/></svg>
      <span>+614 1255 8907</span>
    </div>
    <div class="person-name">Dr Owen Palatsky <strong>PhD MCommrclLaw</strong></div>
    <div class="phone">
      <svg viewBox="0 0 24 24"><path d="M6.6 10.8a15.1 15.1 0 0 0 6.6 6.6l2.2-2.2c.3-.3.7-.4 1-.2 1.1.4 2.3.6 3.6.6.6 0 1 .4 1 1V20c0 .6-.4 1-1 1A17 17 0 0 1 3 4c0-.6.4-1 1-1h3.5c.6 0 1 .4 1 1 0 1.3.2 2.5.6 3.6.1.3 0 .7-.2 1z"/></svg>
      <span>+614 3761 9042</span>
    </div>
  </div>

  <div class="web-contact">
    <div class="row">
      <svg viewBox="0 0 20 14"><rect x="0.5" y="0.5" width="19" height="13" fill="var(--leaf)"/><path d="M0.5 0.5 L10 8 L19.5 0.5 M0.5 13.5 L7.5 6.5 M19.5 13.5 L12.5 6.5" stroke="#fff" stroke-width="1.4" fill="none"/></svg>
      <span>colin@<strong>quorvanmedical</strong>.com.au</span>
    </div>
    <div class="row">
      <svg viewBox="0 0 20 20"><circle cx="10" cy="10" r="8.5" fill="none" stroke="var(--leaf)" stroke-width="1.8"/><ellipse cx="10" cy="10" rx="3.5" ry="8.5" fill="none" stroke="var(--leaf)" stroke-width="1.4"/><path d="M1.5 10h17M3 5.5h14M3 14.5h14" stroke="var(--leaf)" stroke-width="1.4"/></svg>
      <span>www.<strong>quorvanmedical</strong>.com.au</span>
    </div>
  </div>

  <div class="corner-name">Quorvan Medical</div>
</section>

</body>
</html>
```